Talvor GmbH business card

We Talvor GmbH based in Switzerland are looking for a business card design. The Fresh Jung, appealing to customers of all kinds. We already have a logo to upload but still a business card. Details: Talvor GmbH Address: Lindenweg 14b in 9476 Brugwil. Tel: 41 79 462 37 18, web: Talvor.ch, E-mail: info@Talvor.ch Facebook: Talvor GmbH. I am the Managing Director: Luka Petrovac. On reverse: Title: Transporter and bus rental Gross: Without deposit Super prices
Contact Information for Business Card
Siehe Projektbeschreibung
Requirements
Should not have
- Other pictures

```html
<!DOCTYPE html>
<html lang="en">
<head>
<meta charset="UTF-8">
<title>Talvor GmbH – Business Card</title>
<link href="https://fonts.googleapis.com/css2?family=Open+Sans:wght@400;600;700&display=swap" rel="stylesheet">
<style>
  :root {
    --navy: #0b0b78;
    --steel: #7f9ab5;
    --grey-text: #555a66;
    --paper: #ffffff;
    --backdrop: #eceef1;
  }
  * { margin: 0; padding: 0; box-sizing: border-box; }
  html, body {
    width: 1200px;
    height: 900px;
    overflow: hidden;
    background: var(--backdrop);
    font-family: "Open Sans", Arial, sans-serif;
  }
  .canvas { position: relative; width: 1200px; height: 900px; }

  .card {
    position: absolute;
    width: 556px;
    height: 342px;
    background: var(--paper);
    box-shadow: 0 4px 14px rgba(0, 0, 0, 0.12);
    overflow: hidden;
  }
  .card--front { left: 238px; top: 62px; }
  .card--back  { left: 458px; top: 519px; }

  .wordmark {
    color: var(--navy);
    font-weight: 700;
    letter-spacing: 1px;
    line-height: 1;
    white-space: nowrap;
  }
  .card--front .wordmark {
    position: absolute;
    left: 24px;
    top: 26px;
    font-size: 58px;
  }

  .holder { position: absolute; left: 24px; top: 108px; }
  .holder__name { color: var(--navy); font-size: 19px; font-weight: 700; line-height: 1.2; }
  .holder__role { color: var(--grey-text); font-size: 15px; line-height: 1.3; }

  .contact-band {
    position: absolute;
    left: 0;
    top: 157px;
    width: 482px;
    height: 170px;
    background: var(--navy);
    color: #fff;
  }
  .address {
    position: absolute;
    left: 24px;
    top: 22px;
    font-size: 15px;
    line-height: 20px;
  }
  .contact-list {
    position: absolute;
    left: 24px;
    top: 84px;
    list-style: none;
    font-size: 15px;
    line-height: 20px;
  }
  .contact-list li { display: flex; align-items: center; gap: 9px; }
  .contact-list svg { width: 11px; height: 11px; fill: #fff; flex: none; }

  .brand-block {
    position: absolute;
    left: 345px;
    top: 160px;
    width: 150px;
    height: 150px;
    background: var(--steel);
  }

  .back-lockup {
    position: absolute;
    left: 0;
    right: 0;
    top: 142px;
    display: flex;
    justify-content: center;
    align-items: center;
    gap: 14px;
  }
  .back-lockup .brand-square {
    width: 58px;
    height: 58px;
    background: var(--navy);
  }
  .card--back .wordmark { font-size: 46px; }
</style>
</head>
<body>
<main class="canvas">

  <section class="card card--front" aria-label="Business card front">
    <div class="wordmark">Talvor GmbH</div>

    <div class="holder">
      <p class="holder__name">Jonathan Smith</p>
      <p class="holder__role">Managing Director</p>
    </div>

    <div class="contact-band">
      <p class="address">12345, Address Goes Here<br>Country Name, 123456.</p>
      <ul class="contact-list">
        <li>
          <svg viewBox="0 0 24 24" aria-hidden="true"><path d="M6.6 10.8a15.1 15.1 0 0 0 6.6 6.6l2.2-2.2a1 1 0 0 1 1-.25 11.4 11.4 0 0 0 3.6.57 1 1 0 0 1 1 1V20a1 1 0 0 1-1 1A17 17 0 0 1 3 4a1 1 0 0 1 1-1h3.5a1 1 0 0 1 1 1c0 1.25.2 2.46.57 3.6a1 1 0 0 1-.25 1z"/></svg>
          044-123 456 789
        </li>
        <li>
          <svg viewBox="0 0 24 24" aria-hidden="true"><path d="M2 5h20v14H2z M2 5l10 8 10-8" /><path d="M3 6l9 7 9-7v1l-9 7-9-7z" fill="#0b0b78"/></svg>
          info@webname.com
        </li>
        <li>
          <svg viewBox="0 0 24 24" aria-hidden="true"><circle cx="12" cy="12" r="11"/><path d="M7 8l4 1 1 4-3 2zM14 15l3-2 1 4z" fill="#0b0b78"/></svg>
          www.websitename.com
        </li>
      </ul>
    </div>

    <div class="brand-block" aria-hidden="true"></div>
  </section>

  <section class="card card--back" aria-label="Business card back">
    <div class="back-lockup">
      <div class="brand-square" aria-hidden="true"></div>
      <div class="wordmark">Talvor GmbH</div>
    </div>
  </section>

</main>
</body>
</html>
```